Analytics software company needs a business card design

We need a business card design for a global analytics software provider called 'Varnel Software'. Our main focus is developing real estate analysis software. We are open to any color scheme. The final design should be simple, modern, and precise.
Updates

There is one day left in our project and we are still looking forward to receiving additional submissions. We look forward to selecting one of your designs. Thanks.

Industry/Entity Type

Real Estate

```html
<!DOCTYPE html>
<html lang="en">
<head>
<meta charset="utf-8">
<title>Varnel Software – Business Card</title>
<link rel="stylesheet" href="https://fonts.googleapis.com/css2?family=Roboto:wght@300;400;500&display=swap">
<style>
  :root {
    --backdrop: #958b98;
    --card-grey: #9c9a9f;
    --purple: #4f1e93;
    --purple-deep: #3e1578;
    --purple-light: #6a3aab;
    --text-purple: #4a1f8c;
    --text-grey: #b9b6bd;
  }
  * { margin: 0; padding: 0; box-sizing: border-box; }
  html, body {
    width: 1200px; height: 818px; overflow: hidden;
    background: var(--backdrop);
    font-family: "Roboto", Arial, sans-serif;
  }
  .canvas {
    position: relative; width: 1200px; height: 818px;
    display: flex; align-items: center; justify-content: center; gap: 60px;
  }
  .card {
    position: relative; width: 480px; height: 274px; overflow: hidden;
    box-shadow: 0 10px 24px rgba(40, 20, 60, 0.25);
  }
  .card-art { position: absolute; inset: 0; }
  .card-front { background: var(--card-grey); }
  .card-back { background: var(--purple); }

  .brand-name {
    position: absolute; font-weight: 300; font-size: 30px; letter-spacing: 0.5px;
    color: var(--text-purple);
  }
  .card-front .brand-name { left: 52px; top: 88px; }
  .card-back .brand-name { left: 58px; top: 96px; color: var(--text-grey); }

  .holder { position: absolute; right: 30px; top: 28px; text-align: right; color: #2b1a45; }
  .holder-name { font-size: 17px; font-weight: 500; }
  .holder-title { font-size: 10px; margin-top: 3px; }

  .contact {
    position: absolute; right: 30px; top: 110px; text-align: right;
    font-size: 12px; line-height: 1.45; color: var(--text-purple); font-weight: 500;
  }
  .web {
    position: absolute; left: 60px; top: 142px;
    font-size: 16px; font-weight: 500; color: var(--text-grey); letter-spacing: 0.5px;
  }
</style>
</head>
<body>
<main class="canvas">
  <section class="card card-front" aria-label="Card front">
    <svg class="card-art" viewBox="0 0 480 274" aria-hidden="true">
      <defs>
        <linearGradient id="band" x1="0" y1="0" x2="1" y2="0">
          <stop offset="0" stop-color="var(--purple-deep)"/>
          <stop offset="0.55" stop-color="var(--purple-light)"/>
          <stop offset="1" stop-color="var(--purple-deep)"/>
        </linearGradient>
      </defs>
      <path d="M0 140 C 60 230, 200 250, 300 274 L 0 274 Z" fill="url(#band)"/>
      <path d="M0 140 C 60 230, 200 250, 300 274" fill="none" stroke="#c9c6cd" stroke-width="2"/>
    </svg>
    <div class="brand-name">Varnel Software</div>
    <div class="holder">
      <div class="holder-name">Your Name</div>
      <div class="holder-title">Senior Analyst</div>
    </div>
    <div class="contact">
      <div>Phone: 555-014-2876</div>
      <div>Email: info@varnel.example</div>
    </div>
  </section>

  <section class="card card-back" aria-label="Card back">
    <svg class="card-art" viewBox="0 0 480 274" aria-hidden="true">
      <defs>
        <radialGradient id="glow" cx="0.35" cy="0.4" r="0.7">
          <stop offset="0" stop-color="var(--purple-light)"/>
          <stop offset="1" stop-color="var(--purple)"/>
        </radialGradient>
      </defs>
      <rect width="480" height="274" fill="url(#glow)"/>
      <path d="M480 20 C 470 150, 400 230, 250 274" fill="none" stroke="#b9b6bd" stroke-width="4"/>
    </svg>
    <div class="brand-name">Varnel Software</div>
    <div class="web">www.varnel.example</div>
  </section>
</main>
</body>
</html>
```